Business cards for Remote DBA team

Business cards for team offering database administration, consultation, machine learning and AI services. As of now team is using both
www.korvilnet.cz and www.brestmoorlab.cz URLs

Target Market(s)

IT managers

Industry/Entity Type

It Professional

Contact Information for Business Card

Should include logo
name, email, phone, twitter tag

Font styles to use
Sans Serif

Colors

Designer to choose colors to be used in the design.

```html
<!DOCTYPE html>
<html lang="en">
<head>
<meta charset="utf-8">
<title>Brestmoor Lab – Business Cards</title>
<link rel="stylesheet" href="https://fonts.googleapis.com/css2?family=Roboto:wght@400;500;700;900&display=swap">
<style>
  :root{
    --bg:#2b2d31;
    --ink:#1e1f22;
    --card-black:#1d1e20;
    --white:#ffffff;
    --blue:#1f95dc;
    --blue-light:#4cc4f4;
    --blue-back-a:#3fa9e6;
    --blue-back-b:#1e84c9;
    --blue-deep:#1a73b3;
    --grey-light:#e4e6e8;
    --grey-mid:#7b7d80;
    --grey-pattern:#eceef1;
    --text-soft:#d8dadd;
  }
  *{box-sizing:border-box;margin:0;padding:0}
  html,body{width:1200px;height:900px;overflow:hidden}
  body{background:var(--bg);font-family:"Roboto",Arial,sans-serif;position:relative}

  .card{position:absolute;border-radius:18px;overflow:hidden}

  /* ---------- front card ---------- */
  .card-front{left:110px;top:160px;width:360px;height:556px;background:var(--white)}
  .card-front .shapes{position:absolute;inset:0}
  .binary-texture{position:absolute;left:0;top:0;width:360px;height:320px;
    background:linear-gradient(160deg,var(--white) 20%,var(--grey-pattern) 100%)}
  .brand{position:absolute;left:0;right:0;top:92px;display:flex;align-items:center;justify-content:center;gap:12px}
  .brand-dot{width:26px;height:26px;border-radius:50%;background:var(--blue)}
  .brand-name{font-weight:900;font-size:30px;line-height:1;color:var(--blue);letter-spacing:.5px;text-transform:uppercase}
  .handle{position:absolute;left:26px;top:150px;transform-origin:left top;transform:rotate(90deg) translateY(-100%);
    display:flex;align-items:center;gap:8px;font-weight:700;font-size:15px;color:var(--ink);white-space:nowrap}
  .handle-dot{width:12px;height:12px;border-radius:50%;background:var(--blue)}
  .name-tab{position:absolute;right:0;top:302px;width:228px;height:56px;padding-right:22px;text-align:right;color:var(--white)}
  .person-name{font-weight:700;font-size:21px;letter-spacing:.6px;line-height:1.25;padding-top:5px}
  .person-role{font-size:15px;line-height:1.1}
  .contacts{position:absolute;right:18px;top:388px;list-style:none}
  .contacts li{display:flex;align-items:center;justify-content:flex-end;gap:10px;color:var(--text-soft);font-size:15px;height:30px}
  .contact-icon{width:20px;height:20px;border-radius:50%;background:var(--blue);display:flex;align-items:center;justify-content:center}

  /* ---------- back card ---------- */
  .card-back{left:560px;top:272px;width:560px;height:362px;
    background:linear-gradient(135deg,var(--blue-back-a),var(--blue-back-b))}
  .back-watermark{position:absolute;right:30px;bottom:34px;font-weight:900;font-size:72px;line-height:.95;
    color:var(--blue-deep);opacity:.35;text-align:right;text-transform:uppercase}
  .services{position:absolute;left:0;top:58px;list-style:none}
  .service{display:flex;align-items:center;gap:6px;height:40px;margin-bottom:14px}
  .service-icon{width:36px;height:36px;flex:none}
  .service-label{height:32px;display:flex;align-items:center;padding:0 14px;font-weight:700;font-size:19px;
    letter-spacing:.4px;text-transform:uppercase;color:var(--ink)}
  .service--db{margin-left:150px}
  .service--db .service-label{background:var(--blue-light)}
  .service--ml{margin-left:115px}
  .service--ml .service-label{background:var(--blue)}
  .service--ai{margin-left:80px}
  .service--ai .service-label{background:var(--grey-light)}
  .service--consult{margin-left:45px}
  .service--consult .service-label{background:var(--grey-mid)}
</style>
</head>
<body>

<section class="card card-front" aria-label="Business card front">
  <div class="binary-texture" role="img" aria-label="Faint binary digit texture"></div>
  <svg class="shapes" width="360" height="556" viewBox="0 0 360 556" aria-hidden="true">
    <polygon points="0,322 360,240 360,254 0,336" fill="var(--blue)"/>
    <polygon points="0,336 360,254 360,556 0,556" fill="var(--card-black)"/>
    <rect x="132" y="302" width="228" height="56" fill="var(--blue)"/>
  </svg>

  <div class="brand">
    <span class="brand-dot"></span>
    <span class="brand-name">Brestmoor Lab</span>
  </div>

  <div class="handle"><span class="handle-dot"></span>@brestmoorlab</div>

  <div class="name-tab">
    <p class="person-name">MAREK HALVORSEN</p>
    <p class="person-role">Director</p>
  </div>

  <ul class="contacts">
    <li>012 555 0147
      <span class="contact-icon"><svg width="12" height="12" viewBox="0 0 24 24"><path fill="#fff" d="M6.6 10.8a15 15 0 0 0 6.6 6.6l2.2-2.2c.3-.3.7-.4 1-.2 1.1.4 2.3.6 3.6.6.6 0 1 .4 1 1V20c0 .6-.4 1-1 1A17 17 0 0 1 3 4c0-.6.4-1 1-1h3.5c.6 0 1 .4 1 1 0 1.2.2 2.4.6 3.6.1.3 0 .7-.2 1z"/></svg></span></li>
    <li>email@brestmoorlab.cz
      <span class="contact-icon"><svg width="12" height="12" viewBox="0 0 24 24"><rect x="2" y="5" width="20" height="14" rx="2" fill="#fff"/><path d="M3 6l9 7 9-7" stroke="#1f95dc" stroke-width="2" fill="none"/></svg></span></li>
    <li>www.korvilnet.cz
      <span class="contact-icon"><svg width="12" height="12" viewBox="0 0 24 24" fill="none" stroke="#fff" stroke-width="2"><circle cx="12" cy="12" r="9"/><path d="M3 12h18M12 3c3 3 3 15 0 18M12 3c-3 3-3 15 0 18"/></svg></span></li>
    <li>www.brestmoorlab.cz
      <span class="contact-icon"><svg width="12" height="12" viewBox="0 0 24 24" fill="none" stroke="#fff" stroke-width="2"><circle cx="12" cy="12" r="9"/><path d="M3 12h18M12 3c3 3 3 15 0 18M12 3c-3 3-3 15 0 18"/></svg></span></li>
  </ul>
</section>

<section class="card card-back" aria-label="Business card back">
  <p class="back-watermark">Brestmoor<br>Lab</p>
  <ul class="services">
    <li class="service service--db">
      <svg class="service-icon" viewBox="0 0 36 36"><polygon points="18,2 33,10 33,26 18,34 3,26 3,10" fill="var(--blue-light)" stroke="var(--ink)" stroke-width="2"/><path d="M18 9l7 3v6c0 4-3 7-7 9-4-2-7-5-7-9v-6z" fill="none" stroke="var(--ink)" stroke-width="2"/></svg>
      <span class="service-label">Database Administration</span>
    </li>
    <li class="service service--ml">
      <svg class="service-icon" viewBox="0 0 36 36"><polygon points="18,2 33,10 33,26 18,34 3,26 3,10" fill="var(--blue)" stroke="var(--ink)" stroke-width="2"/><path d="M10 11h16v11H16l-4 3v-3h-2z" fill="none" stroke="var(--ink)" stroke-width="2"/><path d="M13 15h10M13 18h7" stroke="var(--ink)" stroke-width="1.5"/></svg>
      <span class="service-label">Machine Learning</span>
    </li>
    <li class="service service--ai">
      <svg class="service-icon" viewBox="0 0 36 36"><polygon points="18,2 33,10 33,26 18,34 3,26 3,10" fill="var(--grey-light)" stroke="var(--ink)" stroke-width="2"/><circle cx="18" cy="18" r="7" fill="none" stroke="var(--ink)" stroke-width="3" stroke-dasharray="3 2"/><circle cx="18" cy="18" r="3" fill="none" stroke="var(--ink)" stroke-width="2"/></svg>
      <span class="service-label">AI Services</span>
    </li>
    <li class="service service--consult">
      <svg class="service-icon" viewBox="0 0 36 36"><polygon points="18,2 33,10 33,26 18,34 3,26 3,10" fill="var(--grey-mid)" stroke="var(--ink)" stroke-width="2"/><circle cx="14" cy="15" r="4" fill="none" stroke="var(--ink)" stroke-width="2"/><circle cx="22" cy="15" r="4" fill="none" stroke="var(--ink)" stroke-width="2"/><circle cx="18" cy="22" r="4" fill="none" stroke="var(--ink)" stroke-width="2"/></svg>
      <span class="service-label">Consultation</span>
    </li>
  </ul>
</section>

</body>
</html>
```